Retro game shop business card design

We need a card designed both front and back. we already have a logo. The business name is called Pocket Forge Works and we work on customizing and modifying old zentaro pix pals. Our website is pocketforgeworks.com

our business cards are often shown in snapwall posts ans should be designed so that you can easy identify and see in am image. @pocketforgeworks.

Target Market(s)

men 13-40

Contact Information for Business Card

should have logo, wesbite, and if possible some artwork related to pix pal mods

Font styles to use
Sans Serif

Colors

Designer to choose colors to be used in the design.

Requirements
Must have
• logo, website url www.pocketforgeworks.com, hastag #pixpalmods, email, support@pocketforgeworks.com. pix pal imagry only (illustration preffered)
Nice to have
• illustrations, graphic design with pix pal mods (see snapwall #pixpalmods)
Should not have
• childlike depictions of pixpals, kids, anything unrelated to pix pal mods, no hands, no bertie, no pixel art

```html
<!DOCTYPE html>
<html lang="en">
<head>
<meta charset="utf-8">
<title>Pocket Forge Works — Business Card</title>
<link rel="stylesheet" href="https://fonts.googleapis.com/css2?family=Montserrat:wght@500;800&family=Quicksand:wght@400;500&display=swap">
<style>
  :root {
    --backdrop: #c9c9c9;
    --card-front: #ffffff;
    --card-back: #231f20;
    --ink: #1a1a1a;
    --ink-soft: #555555;
    --rule: #6a6a6a;
    --emboss: #2e2a2b;
    --emboss-edge: #3a3637;
    --art-tone-a: #262223;
    --art-tone-b: #2b2728;
  }
  * { box-sizing: border-box; margin: 0; padding: 0; }
  html, body { width: 1200px; height: 800px; overflow: hidden; }
  body {
    background: var(--backdrop);
    display: flex;
    align-items: center;
    justify-content: center;
    gap: 40px;
  }
  .card {
    width: 525px;
    height: 300px;
    position: relative;
    overflow: hidden;
    box-shadow: 0 6px 18px rgba(0,0,0,0.18);
  }
  .card--front {
    background: var(--card-front);
    display: flex;
    align-items: center;
  }
  .brand-mark {
    width: 262px;
    padding-left: 50px;
    font-family: "Montserrat", sans-serif;
    font-weight: 800;
    font-size: 30px;
    line-height: 0.95;
    letter-spacing: 1px;
    text-transform: uppercase;
    color: var(--ink);
  }
  .divider {
    width: 1px;
    height: 116px;
    background: var(--rule);
  }
  .contact {
    padding-left: 22px;
    font-family: "Quicksand", sans-serif;
    color: var(--ink-soft);
  }
  .contact__name {
    font-family: "Montserrat", sans-serif;
    font-weight: 500;
    font-size: 15px;
    letter-spacing: 0.6px;
    color: var(--ink);
    text-transform: uppercase;
  }
  .contact__role {
    font-size: 12px;
    color: var(--ink);
    margin-bottom: 12px;
  }
  .contact__list { list-style: none; }
  .contact__item {
    display: flex;
    align-items: center;
    gap: 7px;
    font-size: 11px;
    line-height: 1.45;
    white-space: nowrap;
  }
  .contact__icon { width: 9px; height: 9px; flex: none; fill: var(--ink); }
  .card--back {
    background: var(--card-back);
    display: flex;
    align-items: center;
    justify-content: center;
  }
  .back-artwork {
    position: absolute;
    inset: 0;
    background: radial-gradient(ellipse at 50% 50%, var(--art-tone-b) 0%, var(--art-tone-a) 70%);
  }
  .brand-mark--embossed {
    position: relative;
    width: auto;
    padding: 0;
    font-size: 52px;
    color: var(--emboss);
    text-shadow: 0 1px 0 var(--emboss-edge);
  }
</style>
</head>
<body>
  <section class="card card--front">
    <div class="brand-mark">Pocket<br>Forge<br>Works</div>
    <div class="divider"></div>
    <div class="contact">
      <p class="contact__name">Daniel Reyes</p>
      <p class="contact__role">President</p>
      <ul class="contact__list">
        <li class="contact__item">
          <svg class="contact__icon" viewBox="0 0 10 10"><path d="M0 2h10v6H0z M0 2l5 3.5L10 2" fill="none" stroke="#1a1a1a" stroke-width="1.2"/></svg>
          support@pocketforgeworks.com
        </li>
        <li class="contact__item">
          <svg class="contact__icon" viewBox="0 0 10 10"><circle cx="5" cy="5" r="4.2" fill="none" stroke="#1a1a1a" stroke-width="1.2"/><path d="M1 5h8M5 1c-2 2.5-2 5.5 0 8M5 1c2 2.5 2 5.5 0 8" fill="none" stroke="#1a1a1a" stroke-width="0.9"/></svg>
          www.pocketforgeworks.com
        </li>
        <li class="contact__item">
          <svg class="contact__icon" viewBox="0 0 10 10"><circle cx="5" cy="5" r="4.5"/></svg>
          @pocketforgeworks
        </li>
        <li class="contact__item">
          <svg class="contact__icon" viewBox="0 0 10 10"><rect x="1" y="1" width="8" height="8"/></svg>
          #pixpalmods
        </li>
      </ul>
    </div>
  </section>

  <section class="card card--back">
    <div class="back-artwork" role="img" aria-label="Tone-on-tone artwork of a modded pix pal handheld"></div>
    <div class="brand-mark brand-mark--embossed">Pocket<br>Forge<br>Works</div>
  </section>
</body>
</html>
```